New email newsletter banner needed

Financial services firm need a new banner for a newsletter banner. The old one attached.... Size is 4cm x 16cm and should read "Looking for Options".

Base colors can be Pantone colors 281,644,425,1805,405 and any gradient of those.

Font should be Arial MT

Please note the firm mentioned in the old banner no longer applies

Industry/Entity Type

Financial

Requirements
Should not have
• images of people, multiple images

```html
<!DOCTYPE html>
<html lang="en">
<head>
<meta charset="utf-8">
<title>Looking for Options – Financial Newsletter Banners</title>
<link rel="stylesheet" href="https://fonts.googleapis.com/css2?family=Arimo:wght@400&display=swap">
<style>
  :root {
    --page-bg: #ece8e2;
    --slate: #4c535d;
    --umber: #5a4f49;
    --motif-tint: rgba(255, 255, 255, 0.13);
    --motif-fade: rgba(255, 255, 255, 0);
    --title-ink: #ffffff;
    --tab-fill: #ffffff;
    --tab-ink: #474747;
    --shadow: rgba(40, 30, 20, 0.45);
  }
  * { margin: 0; padding: 0; box-sizing: border-box; }
  html, body {
    width: 1200px;
    height: 900px;
    overflow: hidden;
    background: var(--page-bg);
    font-family: "Arimo", Arial, sans-serif;
  }
  .canvas {
    position: relative;
    width: 1200px;
    height: 900px;
  }
  .banner {
    position: absolute;
    left: 52px;
    width: 1100px;
    height: 276px;
    overflow: hidden;
    box-shadow: 2px 4px 7px var(--shadow);
  }
  .banner--slate { top: 114px; background: var(--slate); }
  .banner--umber { top: 508px; background: var(--umber); }
  .banner__motif {
    position: absolute;
    left: 0;
    top: 14px;
    width: 360px;
    height: 262px;
    background: radial-gradient(ellipse 70% 80% at 40% 65%, var(--motif-tint), var(--motif-fade) 75%);
  }
  .banner__tab {
    position: absolute;
    inset: 0;
    width: 1100px;
    height: 276px;
  }
  .tab { fill: var(--tab-fill); }
  .banner__title {
    position: absolute;
    left: 0;
    width: 1112px;
    top: 80px;
    text-align: center;
    font-weight: 400;
    font-size: 64px;
    line-height: 1;
    color: var(--title-ink);
  }
  .banner__subtitle {
    position: absolute;
    left: 140px;
    width: 830px;
    top: 223px;
    text-align: center;
    font-size: 39px;
    line-height: 1;
    color: var(--tab-ink);
  }
</style>
</head>
<body>
<main class="canvas">
  <section class="banner banner--slate">
    <div class="banner__motif" role="img" aria-label="Faint upward arrow motif"></div>
    <svg class="banner__tab" viewBox="0 0 1100 276" aria-hidden="true">
      <path class="tab" d="M138 276 C 165 240 182 204 236 204 L 884 204 C 936 204 950 240 972 276 Z"/>
    </svg>
    <h1 class="banner__title">Looking for Options</h1>
    <p class="banner__subtitle">Financial Newsletter</p>
  </section>

  <section class="banner banner--umber">
    <div class="banner__motif" role="img" aria-label="Faint upward arrow motif"></div>
    <svg class="banner__tab" viewBox="0 0 1100 276" aria-hidden="true">
      <path class="tab" d="M138 276 C 165 240 182 204 236 204 L 884 204 C 936 204 950 240 972 276 Z"/>
    </svg>
    <h1 class="banner__title">Looking for Options</h1>
    <p class="banner__subtitle">Financial Newsletter</p>
  </section>
</main>
</body>
</html>
```